HLT Crown Business Card Design 2020

Hollis Lane Trades is looking for a business card that is clean and straight to the point but still looks high-end and attractive. We are a team comprised of management and field professionals focused on the high-end residential marketplace. We serve homeowners and trade professionals directly based out of the Metrowest/Dalmere area. We provide client services as well as construction/renovation services.
We are aiming for a black and white feel (white background and black text) and a matte finish with rounded edges.

We want to emphasis our vision of "Properties - Projects - Partners".
Dana Fellmore is the president of HLT

Please include the following areas we service: Dalmere/Saltby/Norrhaven
Please make sure to include Dana's mobile (555) 302 4187 & office number (555) 640 2913, email dana@hollislanetrades.example and website www.hollislanetrades.example

Colors

Designer to choose only greyscale colors for use in the design.

Requirements
Must have
• Include "Properties - Projects - Partners" in design

Include "After Hours Emergency Support # 1800 555 0142" with icon

```html
<!DOCTYPE html>
<html lang="en">
<head>
<meta charset="utf-8">
<title>HLT Crown – Business Card</title>
<link rel="stylesheet" href="https://fonts.googleapis.com/css2?family=Montserrat:wght@500;600;700&family=Lato:ital,wght@0,400;0,700;1,400&display=swap">
<style>
  :root {
    --ink: #262626;
    --ink-soft: #555555;
    --paper: #ffffff;
    --tint: #ebebeb;
  }
  * { margin: 0; padding: 0; box-sizing: border-box; }
  html, body { width: 1200px; height: 751px; overflow: hidden; background: var(--paper); }
  .sheet { position: relative; width: 1200px; height: 751px; font-family: "Lato", sans-serif; color: var(--ink); }
  .abs { position: absolute; }

  .side-panel { left: 70px; top: 62px; width: 178px; height: 282px; background: var(--ink); border-radius: 30px 0 0 30px; }
  .side-rule { left: 257px; top: 62px; width: 4px; height: 282px; background: var(--ink); }
  .tint-right { left: 460px; top: 62px; width: 107px; height: 282px; background: var(--tint); border-radius: 0 30px 30px 0; }
  .tint-left { left: 638px; top: 62px; width: 178px; height: 282px; background: var(--tint); border-radius: 30px 0 0 30px; }

  .wordmark { font-family: "Montserrat", sans-serif; font-weight: 700; text-align: center; line-height: 1; }
  .wordmark .wm-main { display: block; }
  .wordmark .wm-sub { display: block; letter-spacing: 0.12em; white-space: nowrap; }
  .wordmark--panel { left: 70px; top: 82px; width: 178px; color: var(--paper); }
  .wordmark--panel .wm-main { font-size: 52px; }
  .wordmark--panel .wm-sub { font-size: 9px; margin-top: 10px; }
  .wordmark--card { left: 912px; top: 84px; width: 210px; color: var(--ink); }
  .wordmark--card .wm-main { font-size: 62px; }
  .wordmark--card .wm-sub { font-size: 11px; margin-top: 16px; }
  .wordmark--large { width: 300px; color: var(--ink); top: 452px; }
  .wordmark--large .wm-main { font-size: 104px; }
  .wordmark--large .wm-sub { font-size: 17px; margin-top: 26px; }

  .vision { list-style: none; }
  .vision li { position: absolute; display: flex; align-items: center; font-size: 16px; font-weight: 700; height: 24px; white-space: nowrap; }
  .vision svg { width: 24px; height: 24px; margin-right: 14px; flex: none; }
  .vision--dark li { color: var(--paper); left: 102px; }
  .vision--dark svg { fill: none; stroke: var(--paper); }
  .vision--light li { color: var(--ink-soft); left: 962px; }
  .vision--light svg { stroke: var(--ink-soft); fill: none; }

  .person-name { font-family: "Montserrat", sans-serif; font-weight: 700; font-size: 23px; white-space: nowrap; line-height: 1; }
  .person-name--caps { text-transform: uppercase; left: 302px; top: 82px; letter-spacing: 0.01em; }
  .person-name--title { left: 671px; top: 82px; font-weight: 600; }
  .person-role { font-family: "Montserrat", sans-serif; font-weight: 500; font-size: 15px; color: var(--ink-soft); }

  .contact-row { display: flex; align-items: center; font-size: 11px; color: var(--ink-soft); white-space: nowrap; height: 23px; }
  .contact-row .dot { width: 23px; height: 23px; border-radius: 50%; background: var(--ink); margin-right: 10px; flex: none; display: flex; align-items: center; justify-content: center; }
  .contact-row .dot svg { width: 12px; height: 12px; fill: var(--paper); }

  .support { font-size: 11.5px; color: var(--ink-soft); white-space: nowrap; }
  .support .support-label { font-style: italic; display: flex; align-items: center; }
  .support .support-label svg { width: 16px; height: 14px; margin-right: 8px; fill: none; stroke: var(--ink-soft); stroke-width: 2; }
  .support .support-number { font-weight: 700; font-size: 12px; margin-left: 24px; margin-top: 8px; color: var(--ink); }

  .areas { display: flex; gap: 18px; font-size: 15px; color: var(--ink-soft); top: 641px; white-space: nowrap; }
  .areas span::before { content: ""; display: inline-block; width: 7px; height: 7px; border-radius: 50%; background: var(--ink-soft); margin-right: 13px; vertical-align: middle; position: relative; top: 2px; }
</style>
</head>
<body>
<main class="sheet">

  <!-- Card front, dark panel variant -->
  <div class="abs side-panel"></div>
  <div class="abs side-rule"></div>
  <div class="abs tint-right"></div>
  <div class="abs wordmark wordmark--panel"><span class="wm-main">HLT</span><span class="wm-sub">HOLLIS LANE TRADES</span></div>

  <ul class="vision vision--dark">
    <li style="top:191px"><svg viewBox="0 0 24 24" stroke-width="1.6"><rect x="4" y="2" width="16" height="20"/><path d="M8 6h2M12 6h2M8 10h2M12 10h2M8 14h2M12 14h2M10 22v-4h4v4"/></svg>Properties</li>
    <li style="top:231px"><svg viewBox="0 0 24 24" stroke-width="1.6"><path d="M9 2h6l3 3v10H9z"/><path d="M4 9h6l3 3v10H4z"/></svg>Projects</li>
    <li style="top:271px"><svg viewBox="0 0 24 24" style="fill:var(--paper);stroke:none"><circle cx="12" cy="7" r="4"/><circle cx="5" cy="8" r="3"/><circle cx="19" cy="8" r="3"/><path d="M5 22c0-6 3-9 7-9s7 3 7 9z"/><path d="M0 18c0-4 2-6 5-6 1 0 2 .3 2.5 1-2 1.5-3 3-3 5z"/><path d="M24 18c0-4-2-6-5-6-1 0-2 .3-2.5 1 2 1.5 3 3 3 5z"/></svg>Partners</li>
  </ul>

  <div class="abs person-name person-name--caps">Dana Fellmore</div>
  <div class="abs person-role" style="left:302px;top:111px">President</div>

  <div class="abs" style="left:304px;top:150px">
    <div class="contact-row"><span class="dot"><svg viewBox="0 0 12 12"><rect x="3" y="0.5" width="6" height="11" rx="1"/></svg></span>(555) 302 4187</div>
    <div class="contact-row" style="margin-top:10px"><span class="dot"><svg viewBox="0 0 12 12"><path d="M2 1l2.5 0 1 3-1.5 1c.7 1.5 1.7 2.5 3 3l1-1.5 3 1V11c-5 0-9-4-9-9z"/></svg></span>(555) 640 2913</div>
    <div class="contact-row" style="margin-top:10px"><span class="dot"><svg viewBox="0 0 12 12"><path d="M1 2.5h10v1L6 6.5 1 3.5z"/><path d="M1 5l5 3 5-3v4.5H1z"/></svg></span>dana@hollislanetrades.example</div>
    <div class="contact-row" style="margin-top:10px"><span class="dot"><svg viewBox="0 0 12 12"><circle cx="6" cy="6" r="5"/></svg></span>www.hollislanetrades.example</div>
  </div>

  <div class="abs support" style="left:306px;top:288px">
    <div class="support-label"><svg viewBox="0 0 16 14"><path d="M2 12V8a6 6 0 0 1 12 0v4"/><rect x="1" y="9" width="3" height="4" fill="var(--ink-soft)"/><rect x="12" y="9" width="3" height="4" fill="var(--ink-soft)"/></svg>After Hours Emergency Support</div>
    <div class="support-number"># 1800 555 0142</div>
  </div>

  <!-- Card front, light variant -->
  <div class="abs tint-left"></div>
  <div class="abs person-name person-name--title">Dana Fellmore</div>
  <div class="abs person-role" style="left:670px;top:112px">President</div>

  <div class="abs" style="left:672px;top:150px">
    <div class="contact-row"><span class="dot"><svg viewBox="0 0 12 12"><rect x="3" y="0.5" width="6" height="11" rx="1"/></svg></span>(555) 302 4187</div>
    <div class="contact-row" style="margin-top:10px"><span class="dot"><svg viewBox="0 0 12 12"><path d="M2 1l2.5 0 1 3-1.5 1c.7 1.5 1.7 2.5 3 3l1-1.5 3 1V11c-5 0-9-4-9-9z"/></svg></span>(555) 640 2913</div>
    <div class="contact-row" style="margin-top:10px"><span class="dot"><svg viewBox="0 0 12 12"><path d="M1 2.5h10v1L6 6.5 1 3.5z"/><path d="M1 5l5 3 5-3v4.5H1z"/></svg></span>dana@hollislanetrades.example</div>
    <div class="contact-row" style="margin-top:10px"><span class="dot"><svg viewBox="0 0 12 12"><circle cx="6" cy="6" r="5"/></svg></span>www.hollislanetrades.example</div>
  </div>

  <div class="abs support" style="left:674px;top:290px">
    <div class="support-label"><svg viewBox="0 0 16 14"><path d="M2 12V8a6 6 0 0 1 12 0v4"/><rect x="1" y="9" width="3" height="4" fill="var(--ink-soft)"/><rect x="12" y="9" width="3" height="4" fill="var(--ink-soft)"/></svg>After Hours Emergency Support</div>
    <div class="support-number"># 1800 555 0142</div>
  </div>

  <div class="abs wordmark wordmark--card"><span class="wm-main">HLT</span><span class="wm-sub">HOLLIS LANE TRADES</span></div>

  <ul class="vision vision--light">
    <li style="top:201px"><svg viewBox="0 0 24 24" stroke-width="1.6"><rect x="4" y="2" width="16" height="20"/><path d="M8 6h2M12 6h2M8 10h2M12 10h2M8 14h2M12 14h2M10 22v-4h4v4"/></svg>Properties</li>
    <li style="top:241px"><svg viewBox="0 0 24 24" stroke-width="1.6"><path d="M9 2h6l3 3v10H9z"/><path d="M4 9h6l3 3v10H4z"/></svg>Projects</li>
    <li style="top:281px"><svg viewBox="0 0 24 24" style="fill:var(--ink-soft);stroke:none"><circle cx="12" cy="7" r="4"/><circle cx="5" cy="8" r="3"/><circle cx="19" cy="8" r="3"/><path d="M5 22c0-6 3-9 7-9s7 3 7 9z"/><path d="M0 18c0-4 2-6 5-6 1 0 2 .3 2.5 1-2 1.5-3 3-3 5z"/><path d="M24 18c0-4-2-6-5-6-1 0-2 .3-2.5 1 2 1.5 3 3 3 5z"/></svg>Partners</li>
  </ul>

  <!-- Card backs -->
  <div class="abs wordmark wordmark--large" style="left:170px"><span class="wm-main">HLT</span><span class="wm-sub">HOLLIS LANE TRADES</span></div>
  <div class="abs areas" style="left:200px"><span>Dalmere</span><span>Saltby</span><span>Norrhaven</span></div>

  <div class="abs wordmark wordmark--large" style="left:738px"><span class="wm-main">HLT</span><span class="wm-sub">HOLLIS LANE TRADES</span></div>
  <div class="abs areas" style="left:768px"><span>Dalmere</span><span>Saltby</span><span>Norrhaven</span></div>

</main>
</body>
</html>
```